11"x17" Poster for a Treasure Hunt

Summary:
This project is for a poster that will be used to promote a community treasure hunt for kids aged 9-14. This will be the 10th year we have run the treasure hunt. See the files for previous posters we have used (from PixelGuild).

We loved everything about the 2012 design, particularly how all of the elements seem to belong exactly where they are on the poster. Previous years designs just had text blocks thrown on top of a background image which doesn't make a for a good poster; if within a few seconds you don’t have an idea about what even the poster is promoting, and if you can’t read every part of the poster from 6 feet away, the poster isn't working.

Please make the Brookmere Quest Seekers logo a featured part of the design. See the 2012 poster winner where the logo was right at the top and very prominent.

This is the video promoting this years event:
https://www.vidplexa.example/watch?v=Qm7Hx_4pLzA&feature=share

Poster Details:
Title: The Hollow Lantern Night
Size: 11" x 17"
Format: Illustrator (outlined fonts)
Files: See below for the logos for the two organizers and BRQS
Poster Text: Brookmere Quest Seekers
Hollow Lantern Night (new line)
Be the first team to unravel the mystery surrounding the “Hollow Lantern Night” and you will find the hidden treasure chest and claim a fantastic prize!
Youth ages 9-14 are able to participate. Team applications are available on Sept 1st and due ASAP. Space is limited to the first 50 teams.
Presented by Tim Hokusen of Marlowpine Heritage Property Group and Dr. Neil Ostrov of Brookmere Orthodontics
www.BRQuestSeekers.example
October 18th, 2014

Style: Scary, but remember the event is for children. Think 1950's vintage horror poster or even a modern graphic novel cover. The title of the hunt this year is “The Hollow Lantern Night”. The background story is that an event took place in 1929 and the person responsible is back and “haunting” the scene in 2014, so the two time points are linked. The design should reflect the linking of the two time points.
The design I have in mind is this: The “monster” is in the center of the poster, dividing it in two. He is standing in front of a church. The design of the poster is such that everything on the left hand side of the poster is from the 1920’s and everything on the right is from the 2000’s. There should be other items in the poster to indicate the time period, perhaps other pedestrians, automobiles, etc. Use your imagination. The “monster” himself also reflects this; his left hand side dress is from the 1920’s and he is a normal looking man, his right side is the “monster”. Think two-face from the comics (see here: http://vextoria.files.blogsprocket.example/2013/05/27.jpg), but the monster doesn’t have to look as gruesome as he does. In fact, he can be more mysterious, like the figure here in the dark robe: http://quillnexus.example/myblog/wp-content/uploads/2013/09/CloakedShape_zpk8d3f2b7e.jpg

Some of the poster submissions from previous years were way too gruesome with the “monster”. Do keep in mind this event is for children. For good examples, see "BRQS 2012 Winner" below (our favorite to date), and the “BRQS 2013 winner” files below.

**Update 9/2/14
New logo of the organizer Brookmere Orthodontics uploaded. Please use this logo in place of the original Harrow Orthodontics logo. Thank you.

Reason: I meant to make this contest 2 weeks long but accidentally forgot to change the contest duration before submitting payment.

1) A couple new logo files were uploaded. Please use the Brookmere Orthodontics logo instead of the previous Harrow Orthodontics logo. 2) For the central "monster", try to use a hooded dark figure like this one: http://quillnexus.example/myblog/wp-content/uploads/2013/09/CloakedShape_zpk8d3f2b7e.jpg I would still like to see the poster split down the middle with the left side being in the 1920's and the left in the 2000's. Use your imagination. I'm looking forward to seeing what you guys can come up with.

Reason: Please do not rescind any of your designs. I have extended the deadline so that my partner, who is getting back from vacation in 3 days, can have a chance to review the poster designs before we make a final decision. Thank you.

```html
<!DOCTYPE html>
<html lang="en">
<head>
<meta charset="utf-8">
<title>Brookmere Quest Seekers – The Hollow Lantern Night</title>
<link rel="stylesheet" href="https://fonts.googleapis.com/css2?family=Creepster&family=Oswald:wght@400;500;600&display=swap">
<style>
  :root {
    --night: #0b131c;
    --night-mid: #16293a;
    --blood: #d8261c;
    --gold: #f6b51c;
    --yellow: #f3d21a;
    --paper: #f2f2f2;
    --ash: #d9d9d9;
    --wood: #6b3a1c;
    --realty: #3c3f8e;
  }
  * { margin: 0; padding: 0; box-sizing: border-box; }
  html, body { width: 776px; height: 1200px; overflow: hidden; background: var(--night); }
  .poster {
    position: relative; width: 776px; height: 1200px; overflow: hidden;
    font-family: "Oswald", "Arial Narrow", sans-serif; color: var(--paper);
    background: var(--night);
  }
  .scene {
    position: absolute; inset: 0;
    background:
      radial-gradient(ellipse 420px 360px at 480px 320px, rgba(92,128,158,.55), transparent 70%),
      radial-gradient(ellipse 300px 260px at 180px 260px, rgba(40,66,88,.6), transparent 70%),
      linear-gradient(180deg, #101c28 0%, var(--night-mid) 30%, #0e1822 55%, #0a0f15 100%);
  }
  .map-art {
    position: absolute; left: 0; top: 760px; width: 776px; height: 440px;
    background:
      radial-gradient(ellipse 420px 200px at 430px 120px, rgba(120,110,90,.55), transparent 75%),
      linear-gradient(180deg, rgba(91,84,70,0) 0%, rgba(91,84,70,.35) 30%, rgba(20,22,26,.95) 85%);
  }
  .chest-art {
    position: absolute; left: 47px; top: 613px; width: 320px; height: 240px;
    background:
      radial-gradient(ellipse 120px 50px at 170px 70px, rgba(255,200,90,.85), transparent 75%),
      linear-gradient(180deg, #8a5a2a 0%, var(--wood) 45%, #3a2010 100%);
    border-radius: 30px 40px 6px 6px; opacity: .92;
  }

  .sponsor {
    position: absolute; font-size: 13px; font-weight: 500; line-height: 16px;
    color: var(--ash);
  }
  .sponsor--realty { left: 33px; top: 36px; width: 150px; display: flex; gap: 8px; align-items: flex-start; }
  .sponsor--realty .mark { width: 14px; height: 14px; background: var(--realty); flex: none; margin-top: 1px; }
  .sponsor--ortho { right: 33px; top: 40px; width: 110px; text-align: center; }

  .brand { position: absolute; left: 0; right: 0; top: 88px; text-align: center; font-weight: 500; color: var(--paper); }
  .brand__top { font-size: 22px; letter-spacing: 3px; line-height: 26px; }
  .brand__main {
    display: flex; justify-content: center; align-items: center; gap: 22px;
    margin-top: 32px; font-size: 60px; line-height: 64px; letter-spacing: 2px;
  }
  .brand__dot { width: 18px; height: 18px; border-radius: 50%; background: var(--yellow); }
  .brand__rule { position: absolute; left: 160px; right: 156px; top: 125px; border-top: 1px solid var(--ash); }

  .title {
    position: absolute; left: 0; right: 0; top: 285px; text-align: center;
    font-family: "Creepster", "Impact", cursive; font-weight: 400; color: var(--blood);
    font-size: 84px; line-height: 90px; letter-spacing: 3px; white-space: nowrap;
  }
  .date {
    position: absolute; left: 0; right: 0; top: 476px; text-align: center;
    font-size: 32px; font-weight: 500; color: var(--ash); letter-spacing: 1px;
  }
  .lead {
    position: absolute; left: 40px; right: 40px; top: 550px; text-align: center;
    font-size: 15px; font-weight: 500; line-height: 21px; text-transform: uppercase;
  }
  .prize {
    position: absolute; left: 380px; top: 632px; width: 370px; text-align: center;
    font-size: 48px; line-height: 60px; font-weight: 600; color: var(--gold); white-space: nowrap;
  }
  .details {
    position: absolute; left: 420px; top: 752px; width: 290px; text-align: center;
    font-size: 15px; font-weight: 500; line-height: 20px; text-transform: uppercase;
  }
  .limit {
    position: absolute; left: 385px; top: 818px; width: 360px; text-align: center;
    font-size: 16px; font-weight: 600; color: var(--yellow); text-transform: uppercase; white-space: nowrap;
  }
  .map-x { position: absolute; left: 415px; top: 868px; }
  .presenters { position: absolute; left: 0; right: 0; top: 948px; text-align: center; text-transform: uppercase; }
  .presenters h2 { font-size: 16px; font-weight: 600; letter-spacing: 1px; }
  .presenters hr { width: 400px; margin: 8px auto 12px; border: 0; border-top: 1px solid var(--ash); }
  .presenters p { font-size: 13px; font-weight: 500; line-height: 18px; }
  .site {
    position: absolute; left: 0; right: 0; top: 1110px; text-align: center;
    font-size: 38px; line-height: 50px; font-weight: 500; color: var(--paper); white-space: nowrap;
  }
</style>
</head>
<body>
<main class="poster">
  <div class="scene" role="img" aria-label="Dark blue haunted night scene with a gothic building and bare trees"></div>
  <div class="map-art" role="img" aria-label="Old treasure map with compass lying across the lower poster"></div>
  <div class="chest-art" role="img" aria-label="Open wooden treasure chest glowing with gold"></div>

  <div class="sponsor sponsor--realty">
    <span class="mark"></span>
    <span>Marlowpine Heritage Property Group</span>
  </div>
  <div class="sponsor sponsor--ortho">Brookmere Orthodontics</div>

  <header class="brand">
    <div class="brand__top">BROOKMERE</div>
    <div class="brand__main"><span>QUEST</span><span class="brand__dot"></span><span>SEEKERS</span></div>
    <div class="brand__rule"></div>
  </header>

  <h1 class="title">THE HOLLOW<br>LANTERN NIGHT</h1>
  <p class="date">OCTOBER 18TH, 2014</p>

  <p class="lead">Be the first team to unravel the mystery surrounding the “Hollow Lantern Night”<br>and you will find the hidden treasure chest and claim a</p>

  <p class="prize">FANTASTIC PRIZE!</p>
  <p class="details">Youth ages 9-14 are able to participate.<br>Team applications are available<br>on Sept 1st and due ASAP.</p>
  <p class="limit">Space is limited to the first 50 teams.</p>

  <svg class="map-x" width="24" height="24" viewBox="0 0 24 24" aria-hidden="true">
    <path d="M3 3 L21 21 M21 3 L3 21" stroke="#1a1410" stroke-width="4" stroke-linecap="round"/>
  </svg>

  <section class="presenters">
    <h2>Presented by</h2>
    <hr>
    <p>Tim Hokusen of Marlowpine Heritage Property Group and<br>Dr. Neil Ostrov of Brookmere Orthodontics</p>
  </section>

  <p class="site">www.BRQuestSeekers.example</p>
</main>
</body>
</html>
```